Modern and sophisticated web design for architect/designer

Lumo Vant is a Building Design & Drafting studio based in Nedlands Western Australia, providing a high quality and complete client service from concept design through Council planning approvals and building licenses to construction drawings for kitchens and bathrooms, extensions, additions, renovations and new homes.

Lumo Vant is looking for a new qwerty design that *is different from a normal* 2/3 column website. The website design must be very arty, clean and catchy. This design needs to be very different and must not look like a downloadable template.

The design must be able to display a lot of photos for the different projects.

The design must comply with W3C standards (i.e. use of fonts) and must be delivered to us in A PSD layered format.

Here are a couple of example website designs that exemplify what I am after:
1) http://www.prtd.com.au/
2) http://www.martinholsbyarchitect.com/en/
3) http://veromiks.com/

I particularly like numbers 1 and 2. The third, Veromiks, jumps around a little between pages as it is actually several companies. I prefer the page design to remain steady if possible.

I like the very clever nature of number 1 (PRTD). It captures the interest, although slightly gimmicky, however I think it doesn't overpower. Its modern, and visual.

I like the clean elegant design of number 2 (Holsby), it simply delivers everything necessary in a clear intelligent manner, its attractive, menu is clever simple to use and attractive.

I would be very happy to have either of these websites.

here is another one:
4) http://www.tqarchitect.com.au/

Although this is similarly elegant, it appears quite dated. I don't like the thumbnails that you click on in the gallery, its quite clumsy. It looks minimalist, and IS minimalist, doesn't look like there is much option to expand other than changing the pictures.

If you look at my own website:
http://www.lumovant.com.au

I designed and built it myself without any skills or experience. I had to use a generic photo album generator which was worse than useless, the point I am trying to make is I tried to make the menu system a little unusual, I tried to keep the pages neat and tidy, and totally used the "black website" method. However I am more inclined to go with the lighter/white pages of (1) and (2) above because they tend to show photos better.

Dear Designers. 

ArtHive Administration has worked to provide a more comprehensive brief. Please review the amended description. 

Kind Regards, Wesley. 

Target Market(s)

Target market is people who are looking to renovate their home

Industry/Entity Type

Construction

Requirements
Must have
• The brief is to design a visual modern, elegant, sophisticated website for a small scale designer/photographer/architect that looks itself like it is designed. Not off the shelf, simple and dated. Basically the design itself has to exemplify me, it has to say "this guy is a designer, and he is good at it".

```html
<!DOCTYPE html>
<html lang="en">
<head>
<meta charset="utf-8">
<title>Lumo Vant — Building Design &amp; Drafting</title>
<link rel="stylesheet" href="https://fonts.googleapis.com/css2?family=Oswald:wght@300;400&family=Hind:wght@300;400&display=swap">
<style>
  :root {
    --page-bg: #9c8686;
    --page-bg-dark: #8e7878;
    --edge-strip: #efeded;
    --sidebar-bg: #ffffff;
    --nav-active: #2a2222;
    --nav-muted: #9c8686;
    --copy-text: #2a2222;
    --grid-line: #d9cccc;
    --tile-title: #f3cfc6;
    --tile-text: #ffffff;
    --tile-shade: rgba(58, 40, 40, 0.55);
    --corner: #e2cfcf;
    --logo-ink: #3b3434;
  }
  * { box-sizing: border-box; margin: 0; padding: 0; }
  html, body { width: 1200px; height: 571px; overflow: hidden; }
  body {
    position: relative;
    background: repeating-linear-gradient(45deg, var(--page-bg) 0 2px, var(--page-bg-dark) 2px 4px);
    font-family: "Hind", "Helvetica Neue", Arial, sans-serif;
  }
  .edge-strip {
    position: absolute; left: 77px; top: 0; width: 14px; height: 571px;
    background: var(--edge-strip);
  }
  .sidebar {
    position: absolute; left: 91px; top: 0; width: 271px; height: 571px;
    background: var(--sidebar-bg);
  }
  .sidebar-art {
    position: absolute; left: 0; top: 330px; width: 271px; height: 200px;
    background: radial-gradient(ellipse at 40% 60%, rgba(180,170,170,0.22), rgba(255,255,255,0) 70%);
  }
  .logo {
    position: absolute; left: 14px; top: 64px; width: 250px;
    display: flex; align-items: center; gap: 10px;
  }
  .logo-mark { width: 18px; height: 18px; background: var(--logo-ink); flex: none; }
  .logo-name {
    font-family: "Oswald", "Arial Narrow", sans-serif; font-weight: 400;
    font-size: 30px; letter-spacing: 6px; color: var(--logo-ink); text-transform: uppercase;
  }
  .main-nav { position: absolute; left: 0; top: 236px; width: 271px; }
  .main-nav a {
    display: block; text-align: center; text-decoration: none;
    font-size: 13.5px; line-height: 34px; color: var(--nav-muted);
  }
  .main-nav a.is-active { color: var(--nav-active); }
  .copyright {
    position: absolute; left: 16px; top: 546px; font-size: 10.5px; color: var(--copy-text);
  }
  .project-grid {
    position: absolute; left: 362px; top: 0; width: 838px; height: 571px;
    display: grid; grid-template-columns: repeat(3, 1fr); grid-template-rows: repeat(3, 1fr);
    gap: 1px; background: var(--grid-line);
  }
  .project-tile { position: relative; overflow: hidden; }
  .project-photo { position: absolute; inset: 0; }
  .project-tile::after {
    content: ""; position: absolute; inset: 0; background: var(--tile-shade);
  }
  .project-tile.is-hover::after { display: none; }
  .project-caption {
    position: absolute; left: 0; right: 0; top: 52px; z-index: 1;
    text-align: center; padding: 0 30px;
  }
  .project-title {
    font-family: "Oswald", "Arial Narrow", sans-serif; font-weight: 400;
    font-size: 22px; line-height: 32px; color: var(--tile-title);
    text-shadow: 1px 1px 2px rgba(0,0,0,0.5);
  }
  .project-text { font-size: 13px; line-height: 16px; color: var(--tile-text); font-weight: 300; }
  .zoom-icon { position: absolute; left: 128px; top: 82px; z-index: 1; }
  .corner-tab { position: absolute; right: 0; bottom: 0; z-index: 1; }
  .photo-1 { background: linear-gradient(160deg, #8f8282, #5d5050 60%, #7a6a6a); }
  .photo-2 { background: linear-gradient(180deg, #4a3c3c, #6e6262 50%, #3a2e2e); }
  .photo-3 { background: linear-gradient(150deg, #3a2e2e, #5b4d4d 55%, #2e2424); }
  .photo-4 { background: linear-gradient(135deg, #0e1f3d 0%, #2c3550 35%, #a0603a 60%, #e59a3a 80%, #3c5a28 100%); }
  .photo-5 { background: linear-gradient(170deg, #9a8e8e, #7e7070 55%, #6a5c5c); }
  .photo-6 { background: linear-gradient(160deg, #9a8c8c, #6a5b5b 60%, #4e4040); }
  .photo-7 { background: linear-gradient(165deg, #6a5c5c, #3a2e2e 60%, #5a4c4c); }
  .photo-8 { background: linear-gradient(180deg, #8c8080, #a89c9c 50%, #7a6c6c); }
  .photo-9 { background: linear-gradient(180deg, #8a7c7c, #6a5c5c 55%, #7c6e6e); }
</style>
</head>
<body>
  <div class="edge-strip"></div>

  <aside class="sidebar">
    <div class="sidebar-art" role="img" aria-label="Faint sketch of a house over architectural plans"></div>
    <div class="logo">
      <span class="logo-mark"></span>
      <span class="logo-name">Lumo Vant</span>
    </div>
    <nav class="main-nav">
      <a href="#" class="is-active">Home</a>
      <a href="#">About Us</a>
      <a href="#">Services</a>
      <a href="#">Help</a>
      <a href="#">Contact Us</a>
    </nav>
    <p class="copyright">Copyright © 2013 LumoVant. All Rights Reserved.</p>
  </aside>

  <main class="project-grid">
    <article class="project-tile">
      <div class="project-photo photo-1" role="img" aria-label="Modern two-storey house facade"></div>
      <div class="project-caption">
        <h2 class="project-title">Consectetur</h2>
        <p class="project-text">Consectetur adipiscing elit. Etiam eget pretium nulla. Proin eget</p>
      </div>
    </article>
    <article class="project-tile">
      <div class="project-photo photo-2" role="img" aria-label="Contemporary kitchen interior"></div>
      <div class="project-caption">
        <h2 class="project-title">Duis nec</h2>
        <p class="project-text">Donec a lectus non purus ultricies eleifend. Duis nec augue</p>
      </div>
    </article>
    <article class="project-tile">
      <div class="project-photo photo-3" role="img" aria-label="Garden courtyard with plants"></div>
      <div class="project-caption">
        <h2 class="project-title">lorem vestibu</h2>
        <p class="project-text">lectus non purus ultricies eleifend. Duis nec augue eget lorem</p>
      </div>
    </article>

    <article class="project-tile is-hover">
      <div class="project-photo photo-4" role="img" aria-label="Stone-clad house entrance lit at dusk"></div>
      <svg class="zoom-icon" width="26" height="26" viewBox="0 0 26 26" aria-hidden="true">
        <circle cx="10" cy="10" r="7.5" fill="none" stroke="#e8dcd8" stroke-width="2.2"/>
        <line x1="15.5" y1="15.5" x2="23" y2="23" stroke="#e8dcd8" stroke-width="3" stroke-linecap="round"/>
      </svg>
      <svg class="corner-tab" width="40" height="40" viewBox="0 0 40 40" aria-hidden="true">
        <polygon points="40,0 40,40 0,40" fill="var(--corner)"/>
        <line x1="27" y1="31" x2="37" y2="31" stroke="#3b3434" stroke-width="1.4"/>
        <line x1="32" y1="26" x2="32" y2="36" stroke="#3b3434" stroke-width="1.4"/>
      </svg>
    </article>
    <article class="project-tile">
      <div class="project-photo photo-5" role="img" aria-label="House with angled roof"></div>
      <div class="project-caption">
        <h2 class="project-title">Lorem ipsum dolor</h2>
        <p class="project-text">Non purus ultricies eleifend. Duis nec augue eget lorem vesti</p>
      </div>
    </article>
    <article class="project-tile">
      <div class="project-photo photo-6" role="img" aria-label="Timber deck and steps at a home"></div>
      <div class="project-caption">
        <h2 class="project-title">Integer eget</h2>
        <p class="project-text">Adipiscing elit. Etiam eget pretium nulla. Proin eget sapien</p>
      </div>
    </article>

    <article class="project-tile">
      <div class="project-photo photo-7" role="img" aria-label="Curved steel architectural structure"></div>
      <div class="project-caption">
        <h2 class="project-title">Adipiscing elit</h2>
        <p class="project-text">Duis nec augue eget lorem vestibulum suscipit.</p>
      </div>
    </article>
    <article class="project-tile">
      <div class="project-photo photo-8" role="img" aria-label="Bright office interior"></div>
      <div class="project-caption">
        <h2 class="project-title">lectus non</h2>
        <p class="project-text">Adipiscing elit. Etiam eget pretium nulla. Proin eget sapien</p>
      </div>
    </article>
    <article class="project-tile">
      <div class="project-photo photo-9" role="img" aria-label="Living room with large glass walls"></div>
      <div class="project-caption">
        <h2 class="project-title">Vestibulum</h2>
        <p class="project-text">Etiam eget pretium nulla. Proin eget sapien</p>
      </div>
    </article>
  </main>
</body>
</html>
```